female esthetician looking for an impact business card

I an an expert in skin care industry with high experience in NYC.I want my business card to look professional , an impact at first look. I do want a combination between white and gold . I believe the font will be great if is gold.. The Fonts are also important. MIRELA COSTANDI (SKIN CARE BOUTIQUE)

THIS SHOULD BE THE BUSINESS NAME, and should be placed on th eback of the card.
IN front m, the name MIRELA COSTANDI - ESTHETCIAN

BY APPOINTMENTS ONLY: 512.478.2936

Target Market(s)

HIGH END CLIENTELE

Contact Information for Business Card

iT WILL BE on a luxury paper. I neeed the wow feeling

Requirements
Should not have
• pictures

```html
<!DOCTYPE html>
<html lang="en">
<head>
<meta charset="utf-8">
<title>Mirela Costandi – Business Card</title>
<link rel="stylesheet" href="https://fonts.googleapis.com/css2?family=Montserrat:wght@300;400;600&display=swap">
<style>
  :root {
    --backdrop: #1c1c1c;
    --paper: #ffffff;
    --gold-deep: #b8801f;
    --gold-mid: #d9a93a;
    --gold-light: #f3d774;
    --gold-gradient: linear-gradient(120deg, var(--gold-deep) 0%, var(--gold-mid) 45%, var(--gold-light) 75%, var(--gold-mid) 100%);
  }
  * { box-sizing: border-box; margin: 0; padding: 0; }
  html, body { width: 1200px; height: 895px; overflow: hidden; }
  body {
    background: var(--backdrop);
    font-family: "Montserrat", sans-serif;
    position: relative;
  }
  .card {
    position: absolute;
    top: 137px;
    width: 360px;
    height: 620px;
    background: var(--paper);
    box-shadow: 0 18px 40px rgba(0,0,0,.55);
  }
  .card--back { left: 180px; }
  .card--front { left: 660px; }
  .card__frame { position: absolute; left: 0; top: 0; }
  .gold-text {
    background: var(--gold-gradient);
    -webkit-background-clip: text;
    background-clip: text;
    color: transparent;
  }
  .card__name {
    position: absolute;
    left: 48px;
    top: 82px;
    width: 290px;
    font-weight: 600;
    font-size: 27px;
    letter-spacing: .5px;
    white-space: nowrap;
  }
  .card__title {
    position: absolute;
    right: 40px;
    top: 124px;
    font-weight: 300;
    font-size: 17px;
    letter-spacing: 1px;
  }
  .boutique {
    position: absolute;
    right: 30px;
    bottom: 36px;
    font-weight: 300;
    font-size: 17px;
    letter-spacing: .5px;
  }
  .boutique-rule {
    position: absolute;
    right: 30px;
    bottom: 76px;
    width: 70px;
    height: 1.5px;
    background: var(--gold-gradient);
  }
  .contact {
    position: absolute;
    left: 30px;
    bottom: 40px;
  }
  .contact__note {
    font-weight: 300;
    font-size: 16px;
    letter-spacing: .5px;
    margin-left: 120px;
    margin-bottom: 8px;
  }
  .contact__rule {
    width: 62px;
    height: 1.5px;
    background: var(--gold-gradient);
    margin: 0 0 14px 250px;
  }
  .contact__row {
    display: flex;
    align-items: center;
    gap: 10px;
    margin-bottom: 10px;
  }
  .contact__row--phone { margin-left: 90px; }
  .contact__phone { font-weight: 600; font-size: 22px; letter-spacing: 1px; }
  .contact__email { font-weight: 400; font-size: 16px; letter-spacing: .5px; }
  .contact__icon { width: 20px; height: 20px; flex: none; }
</style>
</head>
<body>
  <svg width="0" height="0" style="position:absolute">
    <defs>
      <linearGradient id="gold" x1="0" y1="0" x2="1" y2="1">
        <stop offset="0" stop-color="#b8801f"/>
        <stop offset=".5" stop-color="#d9a93a"/>
        <stop offset="1" stop-color="#f3d774"/>
      </linearGradient>
    </defs>
  </svg>

  <section class="card card--back" aria-label="Card back">
    <svg class="card__frame" width="360" height="620" aria-hidden="true">
      <path d="M40 345 V30 H320 V330 H260 M200 330 H40" fill="none" stroke="url(#gold)" stroke-width="2"/>
    </svg>
    <h1 class="card__name gold-text">MIRELA COSTANDI</h1>
    <div class="boutique-rule"></div>
    <p class="boutique gold-text">SKIN CARE BOUTIQUE</p>
  </section>

  <section class="card card--front" aria-label="Card front">
    <svg class="card__frame" width="360" height="620" aria-hidden="true">
      <path d="M40 345 V30 H320 V330 H260 M200 330 H40" fill="none" stroke="url(#gold)" stroke-width="2"/>
    </svg>
    <h1 class="card__name gold-text">MIRELA COSTANDI</h1>
    <p class="card__title gold-text">Esthetician</p>
    <div class="contact">
      <p class="contact__note gold-text">By appointments only:</p>
      <div class="contact__rule"></div>
      <div class="contact__row contact__row--phone">
        <svg class="contact__icon" viewBox="0 0 24 24" aria-hidden="true">
          <path fill="url(#gold)" d="M6.6 10.8a15.1 15.1 0 0 0 6.6 6.6l2.2-2.2c.3-.3.7-.4 1-.2 1.1.4 2.3.6 3.6.6.6 0 1 .4 1 1V20c0 .6-.4 1-1 1A17 17 0 0 1 3 4c0-.6.4-1 1-1h3.5c.6 0 1 .4 1 1 0 1.3.2 2.5.6 3.6.1.3 0 .7-.2 1z"/>
        </svg>
        <span class="contact__phone gold-text">512.478.2936</span>
      </div>
      <div class="contact__row">
        <svg class="contact__icon" viewBox="0 0 24 24" aria-hidden="true">
          <rect x="2" y="5" width="20" height="14" fill="url(#gold)"/>
          <path d="M2 5 L12 13 L22 5" fill="none" stroke="#fff" stroke-width="1.5"/>
        </svg>
        <span class="contact__email gold-text">mirelacostandi@mailbox.com</span>
      </div>
    </div>
  </section>
</body>
</html>
```